Letterhead and Envelopes design using existing logo. Logo can be found at ridgemontcaldera.example

Use existing logo (attached) and incorporate in letterhead and envelope designs.

Current logo can be viewed at ridgemontcaldera.example the web site reflect various parent and sub companies. Please see attached as well.

Target Market(s)

Other oil and gas operators.

Industry/Entity Type

Oil And Gas

Font styles to use
Sans Serif

Colors

Designer to choose colors to be used in the design.

Requirements
Must have
• Current logo and address
Nice to have
• Modern, contemporary approach yet incorporate existing traditional design.
• After design is selected for Ridgemont Caldera Holdings I will use similar design for Royalties, Exploration, Energy and Farms with different color schemes.

```html
<!DOCTYPE html>
<html lang="en">
<head>
<meta charset="utf-8">
<title>Ridgemont Caldera Holdings Letterhead</title>
<link href="https://fonts.googleapis.com/css2?family=Arimo:wght@400;700&display=swap" rel="stylesheet">
<style>
  :root {
    --backdrop: #45464b;
    --paper: #ffffff;
    --header-top: #d9d4cf;
    --header-bottom: #f7f6f4;
    --accent-green: #8fae5a;
    --navy: #1f3a66;
    --slate: #4d5f75;
    --ink: #1a1a1a;
    --footer-text: #e6eaf0;
  }
  * { box-sizing: border-box; margin: 0; padding: 0; }
  html, body {
    width: 1200px; height: 960px; overflow: hidden;
    background: var(--backdrop);
    font-family: "Arimo", Arial, sans-serif;
  }
  .letterhead {
    position: absolute; left: 290px; top: 60px;
    width: 620px; height: 840px;
    background: var(--paper);
    box-shadow: 0 18px 40px rgba(0,0,0,.35);
    overflow: hidden;
  }
  .letterhead__header {
    position: absolute; left: 0; top: 0; width: 100%; height: 104px;
    background: linear-gradient(to bottom, var(--header-top), var(--header-bottom));
    border-bottom: 1px solid var(--accent-green);
  }
  .letterhead__welcome {
    position: absolute; left: 46px; top: 24px;
    color: var(--navy); text-align: center; line-height: 1.15;
  }
  .letterhead__welcome .line-small { font-size: 15px; }
  .letterhead__welcome .line-name { font-size: 20px; }
  .letterhead__welcome sup { font-size: 8px; }
  .brand-tab {
    position: absolute; right: 40px; top: 0;
    width: 176px; height: 148px;
    background: var(--paper);
    border: 1px solid var(--accent-green); border-top: none;
    border-radius: 0 0 88px 88px;
    display: flex; flex-direction: column; align-items: center; justify-content: center; gap: 8px;
    padding-top: 10px;
  }
  .brand-tab__dot {
    width: 30px; height: 30px; border-radius: 50%;
    background: var(--accent-green);
  }
  .brand-tab__name {
    font-size: 13px; font-weight: 700; color: var(--navy);
    text-align: center; line-height: 1.2; letter-spacing: .04em;
  }
  .letter-body {
    position: absolute; left: 48px; top: 190px; width: 500px;
    color: var(--ink); font-size: 10.5px; line-height: 1.5;
  }
  .letter-body .subject { font-size: 12px; margin-bottom: 22px; }
  .letter-body p { margin-bottom: 16px; }
  .signature-block {
    position: absolute; right: 54px; top: 600px; width: 120px; text-align: center;
  }
  .signature-block__mark {
    width: 120px; height: 52px;
    background: linear-gradient(to bottom, #ffffff, #f1f1f1);
    border-bottom: 1px solid #888;
  }
  .signature-block__label { font-size: 12px; color: var(--ink); margin-top: 6px; }
  .letterhead__footer {
    position: absolute; left: 0; bottom: 0; width: 100%; height: 166px;
    background: var(--slate);
    border-top: 3px solid var(--accent-green);
    color: var(--footer-text); font-size: 12px; line-height: 1.35;
  }
  .footer-address { position: absolute; left: 48px; bottom: 34px; font-style: normal; }
  .footer-contact { position: absolute; right: 54px; top: 18px; text-align: right; }
</style>
</head>
<body>
  <article class="letterhead">
    <header class="letterhead__header">
      <div class="letterhead__welcome">
        <div class="line-small">Welcome to the</div>
        <div class="line-name">Ridgemont Caldera Holdings<sup>®</sup></div>
        <div class="line-small">companies.</div>
      </div>
    </header>
    <div class="brand-tab">
      <span class="brand-tab__dot"></span>
      <span class="brand-tab__name">RIDGEMONT CALDERA<br>HOLDINGS</span>
    </div>

    <section class="letter-body">
      <p class="subject">Subject Line: Loreum ipsum dolor sit amet.</p>
      <p>Lorem ipsum dolor sit amet, consectetur adipiscing elit. Maecenas at dapibus diam. Vivamus fringilla nulla lorem, sit amet mollis nisi suscipit in. Donec lacus tortor, finibus eget pharetra vitae, auctor eget augue. Mauris euismod libero ac risus fermentum, sed rhoncus erat consectetur. Phasellus eget hendrerit ligula, id volutpat tellus. Praesent viverra sapien at convallis eleifend. Pellentesque ac ipsum felis. Vestibulum augue massa, blandit eu tellus eu, fringilla volutpat quam.</p>
      <p>Nulla in neque sit amet diam lobortis lacinia. Donec tristique tristique ex in fermentum. Donec tristique erat non turpis sollicitudin, et posuere dui congue. Nulla elementum finibus orci, in varius ligula feugiat ut. Donec viverra hendrerit est, quis pulvinar metus pretium et. Lorem ipsum dolor sit amet, consectetur adipiscing elit. Nulla tempus pretium convallis. Nunc imperdiet tempus sem sit amet rutrum. Morbi tempus in lacus sed sollicitudin. Praesent non sem commodo, faucibus metus id, imperdiet odio. Morbi sodales convallis nulla a rutrum. Class aptent taciti sociosqu ad litora torquent per conubia nostra, per inceptos himenaeos. Nulla condimentum iaculis tellus non scelerisque. Fusce lobortis gravida pretium.</p>
      <p>Cras nec quam mauris. Nulla eu urna eu tortor bibendum eleifend. Nulla imperdiet semper ex, ac iaculis massa consequat eget. Maecenas quis dui varius, tincidunt massa vitae, condimentum lacus. Aliquam in viverra lorem. Integer eros tortor, tristique ac quam in, tempor accumsan lectus. Nulla in neque tellus.</p>
    </section>

    <div class="signature-block">
      <div class="signature-block__mark" role="img" aria-label="Handwritten signature"></div>
      <div class="signature-block__label">Signature</div>
    </div>

    <footer class="letterhead__footer">
      <address class="footer-address">
        Ridgemont Caldera Holdings, LLC.<br>
        PO Box 318 Larkfield,<br>
        North Dakota 58990
      </address>
      <div class="footer-contact">
        (555) 014.2290<br>
        reception@ridgemontcaldera.example<br>
        www.ridgemontcaldera.example
      </div>
    </footer>
  </article>
</body>
</html>
```